Tall Fern Software

We are a software company selling endpoint visibility, access and security technology to enterprise-level IT departments.

Our technology helps organizations gain comprehensive visibility into and control over devices accessing their corporate network so they can quickly identify and address suspicious activity on the network that could lead to potential threats like data breaches.

This technology can cost organizations upwards of $1M - depending on the size of the organization. Our primary clients are Pinnacle 2,000 companies.

We want a professional, polished business card to represent our new brand.

Info fields to include on the card:
Name
Job Title
Office Phone #
Cell Phone #
Email address
Address: 4217 Westbrook Ridge Blvd., Ste. 2600, Larkhaven, CO 55918
Website address: www.tallfernsoftware.example
Tagline: Discover the edge. Optimize the whole.

Logo files and color specs document are attached. Would like color scheme to coordinate with the logo.

Also looking at stationary/envelope designs in conjunction with the business card designs. Received very few designs that included the stationary.

```html
<!DOCTYPE html>
<html lang="en">
<head>
<meta charset="utf-8">
<title>Tall Fern Software – Business Card</title>
<link rel="stylesheet" href="https://fonts.googleapis.com/css2?family=Jost:wght@400;500;600&family=Roboto+Condensed:wght@300;400&display=swap">
<style>
  :root {
    --page: #ffffff;
    --black: #000000;
    --ink: #1f1f1f;
    --band: #2e2e2e;
    --grey-light: #e6e6e6;
    --grey-mid: #c4c4c4;
    --grey-dark: #9c9c9c;
    --accent: #f0931e;
    --muted: #b5b5b5;
    --contact: #c9c9c9;
  }
  * { margin: 0; padding: 0; box-sizing: border-box; }
  html, body { width: 1200px; height: 1200px; overflow: hidden; background: var(--page); }
  .canvas { position: relative; width: 1200px; height: 1200px; }

  .card {
    position: absolute;
    left: 315px;
    width: 545px;
    height: 302px;
    border: 1px solid #3a3a3a;
    box-shadow: 7px 8px 9px rgba(0,0,0,0.35);
    overflow: hidden;
  }

  /* Front */
  .card-front { top: 220px; background: var(--black); }
  .front-head {
    position: absolute; left: 0; top: 0; width: 100%; height: 101px;
    background: linear-gradient(100deg, var(--grey-dark) 0%, var(--grey-mid) 45%, var(--grey-light) 100%);
  }
  .front-rule {
    position: absolute; left: 0; top: 100px; width: 100%; height: 3px; background: var(--accent);
  }
  .front-swoosh { position: absolute; left: 0; top: 103px; width: 545px; height: 50px; }

  .brand { position: absolute; display: flex; align-items: center; gap: 12px; }
  .brand-mark { width: 30px; height: 30px; background: var(--accent); }
  .brand-name {
    font-family: "Jost", sans-serif; font-weight: 600; color: var(--ink);
    text-transform: uppercase; line-height: 1;
  }
  .brand-name span { display: block; }
  .front-brand { left: 27px; top: 22px; }
  .front-brand .brand-name { font-size: 25px; letter-spacing: 1px; }
  .front-brand .brand-name span + span { font-size: 15px; letter-spacing: 6px; margin-top: 3px; }

  .company-name {
    position: absolute; left: 325px; top: 155px;
    font-family: "Roboto Condensed", sans-serif; font-weight: 400;
    font-size: 21px; letter-spacing: 1px; color: var(--muted);
  }
  .contact {
    position: absolute; left: 326px; top: 200px;
    border-left: 2px solid #8a8a8a; padding-left: 10px;
    font-family: "Roboto Condensed", sans-serif; font-weight: 300; font-style: normal;
    font-size: 11.5px; line-height: 15px; color: var(--contact);
  }

  /* Back */
  .card-back {
    top: 600px;
    background: linear-gradient(110deg, var(--grey-dark) 0%, var(--grey-mid) 45%, var(--grey-light) 100%);
  }
  .back-brand { left: 125px; top: 28px; }
  .back-brand .brand-name { font-size: 30px; letter-spacing: 1px; }
  .back-brand .brand-name span + span { font-size: 17px; letter-spacing: 7px; margin-top: 3px; }
  .back-rule {
    position: absolute; left: 0; top: 100px; width: 100%; height: 3px; background: var(--accent);
  }
  .address, .website {
    position: absolute; left: 0; width: 100%; text-align: center;
    font-family: "Jost", sans-serif; font-weight: 400; color: var(--ink);
  }
  .address { top: 107px; font-size: 14px; letter-spacing: 0.3px; }
  .website { top: 260px; font-size: 18px; letter-spacing: 0.6px; }
</style>
</head>
<body>
<main class="canvas">

  <section class="card card-front" aria-label="Business card front">
    <div class="front-head"></div>
    <div class="front-rule"></div>
    <svg class="front-swoosh" viewBox="0 0 545 50" preserveAspectRatio="none" aria-hidden="true">
      <path d="M0 0 H545 V42 C420 20 240 12 0 14 Z" fill="var(--band)"/>
      <path d="M0 14 C240 12 420 20 545 42 V50 C420 28 240 20 0 22 Z" fill="#1a1a1a"/>
    </svg>
    <div class="brand front-brand">
      <div class="brand-mark"></div>
      <div class="brand-name"><span>Tall Fern</span><span>Software</span></div>
    </div>
    <h2 class="company-name">COMPANY NAME</h2>
    <address class="contact">
      <div>Address: Text text text text</div>
      <div>Tel .:+00 000 000 00 00</div>
      <div>Mob.:+00 000 000 00 00</div>
      <div>e-maile: office@sample.example</div>
    </address>
  </section>

  <section class="card card-back" aria-label="Business card back">
    <div class="brand back-brand">
      <div class="brand-mark"></div>
      <div class="brand-name"><span>Tall Fern</span><span>Software</span></div>
    </div>
    <div class="back-rule"></div>
    <p class="address">4217 Westbrook Ridge Blvd., Ste. 2600, Larkhaven, CO 55918</p>
    <p class="website">www.tallfernsoftware.example</p>
  </section>

</main>
</body>
</html>
```